Heating and Air Conditioning Company Van

This will be the first van in my fleet that I am getting wrapped. Looking to utilize the colors in the motorcycle pic and possibly add some hints of red for heating (or maybe not). I am looking for a full wrap design.

My company does heating and air conditioning with a focus on energy efficient systems. I want to convey the energy efficiency with the green and blue but also want it to look like an HVAC truck (usually red and blue), but also want to stand out from the rest of the HVAC companies.

Ive also attached a picture of a van wrap that somebody else did for me that I kind of like but don't love.

```html
<!DOCTYPE html>
<html lang="en">
<head>
<meta charset="utf-8">
<title>Verdant Heating &amp; Air Conditioning – Rear Door Wrap</title>
<link rel="stylesheet" href="https://fonts.googleapis.com/css2?family=Lato:wght@400;900&family=Saira:ital,wght@0,700;1,800&display=swap">
<style>
  :root {
    --brand-blue: #0f4c97;
    --brand-green: #a6e22e;
    --panel-white: #ffffff;
    --stage: #f1f2f4;
  }
  * { margin: 0; padding: 0; box-sizing: border-box; }
  html, body { width: 942px; height: 1200px; overflow: hidden; background: var(--stage); }
  .wrap-panel {
    position: relative;
    width: 942px;
    height: 1200px;
    background: var(--panel-white);
    overflow: hidden;
  }
  .header-band { position: absolute; left: 0; top: 0; width: 942px; height: 400px; }
  .header-text {
    position: absolute; left: 0; right: 0; top: 172px;
    text-align: center;
    font-family: "Lato", sans-serif; font-weight: 900;
    font-size: 31px; line-height: 36px; letter-spacing: 0.5px;
    color: var(--brand-blue);
  }
  .header-phone {
    position: absolute; left: 0; right: 0; top: 272px;
    display: flex; justify-content: center; align-items: center; gap: 12px;
    font-family: "Saira", sans-serif; font-style: italic; font-weight: 800;
    font-size: 40px; line-height: 50px; color: var(--brand-blue); letter-spacing: 1px;
  }
  .header-phone svg { width: 30px; height: 30px; flex: none; }
  .company-name {
    position: absolute; left: 0; right: 0; top: 396px;
    text-align: center;
    color: var(--brand-blue);
  }
  .company-name .name-main {
    display: block;
    font-family: "Saira", sans-serif; font-style: italic; font-weight: 800;
    font-size: 96px; line-height: 100px; letter-spacing: -1px;
  }
  .company-name .name-trade {
    display: block;
    font-family: "Lato", sans-serif; font-weight: 400;
    font-size: 34px; line-height: 40px; letter-spacing: 0.5px;
  }
  .accent-stripe {
    position: absolute; left: 0; top: 574px; width: 942px; height: 16px;
    background: var(--brand-green);
  }
  .lower-band {
    position: absolute; left: 0; top: 604px; width: 942px; height: 596px;
    background: var(--brand-blue);
  }
  .brand-mark {
    position: absolute; left: 552px; top: 618px;
    width: 172px; height: 172px;
    background: var(--brand-green);
    display: flex; align-items: center; justify-content: center;
    font-family: "Saira", sans-serif; font-style: italic; font-weight: 800;
    font-size: 36px; color: var(--brand-blue);
  }
  .support-badge {
    position: absolute; left: 268px; top: 712px;
    display: flex; align-items: center; gap: 4px;
    color: var(--panel-white);
    font-family: "Saira", sans-serif; font-style: italic; font-weight: 800;
  }
  .support-badge svg { width: 62px; height: 62px; }
  .support-badge .hours { display: block; font-size: 30px; line-height: 30px; }
  .support-badge .label { display: block; font-size: 14px; line-height: 16px; letter-spacing: 0.5px; }
  .web-address {
    position: absolute; left: 0; right: 0; top: 806px;
    text-align: center;
    font-family: "Saira", sans-serif; font-style: italic; font-weight: 800;
    font-size: 38px; color: var(--brand-green); letter-spacing: 0.5px;
  }
</style>
</head>
<body>
<main class="wrap-panel">
  <svg class="header-band" viewBox="0 0 942 400" aria-hidden="true">
    <path d="M176 130 L262 318 Q276 348 306 348 L636 348 Q666 348 680 318 L766 130"
          fill="none" stroke="var(--brand-blue)" stroke-width="16"/>
    <path d="M196 130 L278 308 Q290 332 314 332 L628 332 Q652 332 664 308 L746 130 Z"
          fill="var(--brand-green)"/>
  </svg>

  <p class="header-text">YOUR TRUSTED<br>HVAC INSTALLERS</p>

  <p class="header-phone">
    <svg viewBox="0 0 24 24" aria-hidden="true">
      <circle cx="12" cy="12" r="11" fill="var(--panel-white)"/>
      <path d="M8.2 6.5l1.6-.4 1.2 2.8-1.1 .9c.6 1.4 1.7 2.5 3.1 3.1l.9-1.1 2.8 1.2-.4 1.6c-.2.7-.9 1.1-1.6 1-3.6-.6-6.4-3.4-7-7-.1-.7.3-1.4.5-2.1z" fill="var(--brand-blue)"/>
    </svg>
    914-555-0148
  </p>

  <h1 class="company-name">
    <span class="name-main">Verdant</span>
    <span class="name-trade">HEATING &amp; AIR CONDITIONING</span>
  </h1>

  <div class="accent-stripe"></div>
  <div class="lower-band"></div>

  <div class="brand-mark">Verdant</div>

  <div class="support-badge">
    <svg viewBox="0 0 60 60" aria-hidden="true">
      <path d="M50 30 A20 20 0 1 1 30 10" fill="none" stroke="var(--brand-green)" stroke-width="5"/>
      <path d="M30 3 L39 10 L30 17 Z" fill="var(--brand-green)"/>
      <path d="M30 20 V32 H40" fill="none" stroke="var(--panel-white)" stroke-width="4"/>
    </svg>
    <div>
      <span class="hours">24/7</span>
      <span class="label">SUPPORT</span>
    </div>
  </div>

  <p class="web-address">verdantheatingandac.com</p>
</main>
</body>
</html>
```